Web Design for historic veg friendly, organic restaurant

We need a new web site. The Millbrook Cafe is a 40 year old restaurant in Chicago. We've been one of the premier, casual vegetarian restaurants since we opened. 5 years ago, Millbrook Cafe was purchased from the original owners by a local, certified organic farmer. We are nearly 100% from scratch kitchen, 100% certified organic produce, we are governed by a strict sustainable plan and we are very active politically. But you wouldn't know it form our website! We have a desire to build a simple website around some basic principles:
1. We need our current logo prominently displayed (logo attached)
2. We need a "click to call" easily accessible
3. We have an online order link that needs to be easily accessible
4. We need our hours, location, and directions easy to see
4. We need a separate events page (we have a live music and events venue that runs shows 5-7 nights per week.)
5. We would like to have a separate page for pictures, particularly old pictures. It would be fun to have a function for people to post their own shots, but that might make this too complicated. If it were possible, we would of course need to retain the ability to curate posted pictures.
6. This needs to be easily edited by us, so in a platform such as word press or similar
7. We will need this mobile enhanced

Target Market(s)

Neighborhood residents - zip code is 48213

Industry/Entity Type

Restaurant

Coding

Coded - Design and coding required

Number of Pages Required

4 page

Font styles to use
Sans Serif

Requirements
Must have
• Logo, click to call, events page that we can manage, contact us, about us page, menu (we have the online menu through a third party plugin), a page for our market and some nice pictures on our splash page,
• Must be mobile ready and on a platform such as Word Press or some other platform where we can edit on our own
Nice to have
• Page for past employees and historical pictures, be nice to have food pictures or something similar on a scroll, would love to have an ability for others to post pictures that we would "approve"
Should not have
• We don't need anything that spins, moves, flames or other features that detract from gathering information

```html
<!DOCTYPE html>
<html lang="en">
<head>
<meta charset="utf-8">
<title>Millbrook Cafe</title>
<link href="https://fonts.googleapis.com/css2?family=Alegreya:ital,wght@1,500;1,700&family=Poiret+One&family=Quicksand:wght@400;500;700&display=swap" rel="stylesheet">
<style>
:root{
  --red:#e8403a;
  --red-dark:#c9312b;
  --yellow:#f7b916;
  --yellow-deep:#e9a40c;
  --ink:#2b2b2b;
  --muted:#8a8a8a;
  --white:#ffffff;
  --night:#1b1612;
  --grey-field:#ececec;
}
*{margin:0;padding:0;box-sizing:border-box}
html,body{width:1200px;height:4027px;overflow:hidden}
body{font-family:"Quicksand",sans-serif;color:var(--ink);background:var(--white);position:relative}
.section{position:absolute;left:0;width:1200px;overflow:hidden}
.abs{position:absolute}
.script{font-family:"Alegreya",serif;font-style:italic;font-weight:700}
.btn{position:absolute;background:var(--red);color:var(--white);border-radius:30px;display:flex;align-items:center;justify-content:center;font-size:17px;font-weight:700;letter-spacing:.5px;text-transform:uppercase}
.photo{position:absolute}
/* header */
.topbar{top:0;height:107px;background:linear-gradient(90deg,#f2b31a,#f7c640 45%,#eeaa12)}
.call-label{left:142px;top:30px;font-size:15px;color:var(--red);font-weight:500}
.call-number{left:142px;top:52px;font-size:27px;font-weight:700;color:var(--ink)}
.brand-disc{position:absolute;left:502px;top:4px;width:196px;height:196px;border-radius:50%;background:var(--white);border:6px solid var(--yellow);z-index:5;display:flex;align-items:center;justify-content:center;text-align:center}
.brand-name{font-family:"Alegreya",serif;font-style:italic;font-weight:700;font-size:34px;line-height:1.05;color:var(--red)}
.navbar{top:107px;height:65px;background:var(--white);border-bottom:1px solid #eee}
.nav-item{position:absolute;top:22px;font-size:15px;font-weight:500;color:var(--ink);display:flex;align-items:center;gap:8px;text-transform:uppercase}
.nav-item.active{color:var(--red)}
.nav-item svg{width:18px;height:18px}
/* hero */
.hero{top:172px;height:521px}
.hero-title{left:80px;top:130px;font-family:"Poiret One",sans-serif;font-size:50px;line-height:62px;color:var(--white);font-weight:400}
.search{position:absolute;left:80px;top:351px;width:468px;height:54px;display:flex}
.search-field{flex:1;background:var(--white);padding:0 18px;display:flex;align-items:center;color:#888;font-size:16px}
.search-btn{width:59px;background:var(--yellow);display:flex;align-items:center;justify-content:center}
/* offers strip */
.offers{top:693px;height:167px;background:var(--red)}
.offer-kicker{font-family:"Alegreya",serif;font-style:italic;font-size:18px;color:var(--yellow);top:40px;text-transform:uppercase}
.offer-title{font-family:"Alegreya",serif;font-style:italic;font-weight:700;font-size:22px;color:var(--white);top:80px;text-transform:uppercase}
.offer-line{font-size:17px;color:var(--white);top:112px;font-weight:500}
/* welcome */
.welcome{top:860px;height:630px;background:var(--white)}
.section-title{position:absolute;left:0;width:100%;text-align:center;font-family:"Alegreya",serif;font-style:italic;font-weight:700;font-size:46px}
.section-title .lead{color:var(--yellow)}
.section-title .tail{color:var(--ink)}
.on-dark .tail{color:var(--white)}
.intro-col{position:absolute;top:365px;width:440px;font-size:13.5px;line-height:28px;color:var(--muted);text-align:center}
/* menu */
.menu{top:1490px;height:623px}
.menu-grid{position:absolute;left:80px;top:137px;width:1040px;height:419px;display:grid;grid-template-columns:repeat(3,1fr);grid-template-rows:repeat(2,1fr)}
.menu-tile{display:flex;flex-direction:column;align-items:center;justify-content:center;color:var(--white);text-align:center}
.menu-tile.yellow{background:var(--yellow)}
.menu-tile.red{background:var(--red)}
.menu-tile h3{font-family:"Alegreya",serif;font-weight:700;font-style:normal;font-size:25px;letter-spacing:1px;text-transform:uppercase}
.menu-tile p{font-size:15px;margin-top:8px;font-weight:500}
/* hours */
.hours{top:2113px;height:210px;background:var(--red)}
.hours-title{left:80px;top:45px;font-size:48px}
.hours-title .lead{color:var(--yellow)}
.hours-title .tail{color:var(--white)}
.hours-text{left:80px;top:128px;width:440px;font-size:14px;line-height:24px;color:#ffe6e4}
.hours-row{position:absolute;left:714px;font-size:16px;color:var(--white);font-weight:500}
.hours-row span{position:absolute;left:139px;white-space:nowrap}
/* events */
.events{top:2323px;height:585px;background:var(--white)}
.event{position:absolute;top:123px;width:331px}
.event-photo{position:absolute;left:0;top:0;width:331px;height:207px}
.event-date{position:absolute;left:0;top:191px;width:76px;height:80px;background:var(--yellow);color:var(--white);text-align:center;padding-top:10px}
.event-date b{display:block;font-family:"Alegreya",serif;font-size:34px;line-height:36px;font-weight:700;font-style:normal}
.event-date small{font-size:14px}
.event-title{position:absolute;left:95px;top:222px;width:236px;font-family:"Alegreya",serif;font-style:italic;font-weight:700;font-size:19px;line-height:24px;color:var(--ink)}
.event-body{position:absolute;left:0;top:290px;width:331px;font-size:13.5px;line-height:23px;color:var(--muted)}
.event-more{position:absolute;left:0;top:382px;font-size:14px;font-weight:700;color:var(--red);text-transform:uppercase}
/* gallery */
.gallery{top:2908px;height:521px}
.gallery-row{position:absolute;left:0;top:150px;width:1200px;height:229px;display:flex}
.gallery-row .photo{position:relative;flex:1}
/* newsletter */
.newsletter{top:3429px;height:177px;background:var(--white)}
.news-title{left:129px;top:60px;font-size:44px}
.news-title .lead{color:var(--yellow)}
.news-field{position:absolute;left:416px;top:61px;width:470px;height:57px;border-radius:30px;background:var(--grey-field);display:flex;align-items:center;justify-content:space-between;padding:0 24px;font-size:15px;color:#777}
/* footer */
.footer{top:3606px;height:421px}
.footer-brand{position:absolute;left:451px;top:70px;width:295px;height:170px;display:flex;align-items:center;justify-content:center;gap:14px}
.footer-brand .brand-name{font-size:46px;color:var(--ink)}
.social{position:absolute;top:244px;width:48px;height:48px;border-radius:50%;background:var(--red)}
.footer-links{position:absolute;left:0;top:312px;width:1200px;display:flex;justify-content:center;gap:0;font-size:14px;color:var(--ink);font-weight:500}
.footer-links span{padding:0 28px;border-left:1px solid rgba(0,0,0,.35)}
.footer-links span:first-child{border-left:none}
.copyright{position:absolute;left:0;top:345px;width:1200px;text-align:center;font-size:14px;color:var(--ink)}
</style>
</head>
<body>

<!-- Header -->
<header class="section topbar">
  <svg class="abs" style="left:80px;top:30px" width="46" height="46" viewBox="0 0 24 24" aria-hidden="true"><path fill="#e8403a" d="M6.6 10.8c1.4 2.8 3.8 5.1 6.6 6.6l2.2-2.2c.3-.3.7-.4 1-.2 1.1.4 2.3.6 3.6.6.6 0 1 .4 1 1V20c0 .6-.4 1-1 1C10.6 21 3 13.4 3 4c0-.6.4-1 1-1h3.5c.6 0 1 .4 1 1 0 1.3.2 2.5.6 3.6.1.3 0 .7-.2 1z"/></svg>
  <div class="abs call-label">Call Us On :</div>
  <div class="abs call-number">555 014 7890</div>
  <div class="btn" style="left:953px;top:27px;width:169px;height:59px">Order Now</div>
</header>
<div class="brand-disc"><span class="brand-name">Millbrook<br>Cafe</span></div>

<nav class="section navbar">
  <div class="nav-item active" style="left:80px"><svg viewBox="0 0 24 24"><path fill="none" stroke="#e8403a" stroke-width="2" d="M3 11l9-8 9 8v10h-6v-6H9v6H3z"/></svg>Home</div>
  <div class="nav-item" style="left:183px"><svg viewBox="0 0 24 24"><circle cx="12" cy="8" r="4" fill="#e8403a"/><path d="M4 21c0-4.4 3.6-7 8-7s8 2.6 8 7z" fill="#e8403a"/></svg>About</div>
  <div class="nav-item" style="left:295px"><svg viewBox="0 0 24 24"><path stroke="#e8403a" stroke-width="2.5" d="M3 6h18M3 12h18M3 18h18"/></svg>Menu</div>
  <div class="nav-item" style="left:390px"><svg viewBox="0 0 24 24"><rect x="3" y="5" width="18" height="16" fill="none" stroke="#e8403a" stroke-width="2"/><path stroke="#e8403a" stroke-width="2" d="M3 10h18M8 3v4M16 3v4"/></svg>Events</div>
  <div class="nav-item" style="left:725px"><svg viewBox="0 0 24 24"><rect x="3" y="6" width="18" height="14" rx="2" fill="none" stroke="#e8403a" stroke-width="2"/><circle cx="12" cy="13" r="3.5" fill="none" stroke="#e8403a" stroke-width="2"/></svg>Gallery</div>
  <div class="nav-item" style="left:854px"><svg viewBox="0 0 24 24"><path fill="none" stroke="#e8403a" stroke-width="2" d="M2 4h3l3 11h11l2-8H6"/><circle cx="9" cy="19" r="1.6" fill="#e8403a"/><circle cx="17" cy="19" r="1.6" fill="#e8403a"/></svg>Online Order</div>
  <div class="nav-item" style="left:1020px"><svg viewBox="0 0 24 24"><path fill="#e8403a" d="M6.6 10.8c1.4 2.8 3.8 5.1 6.6 6.6l2.2-2.2c.3-.3.7-.4 1-.2 1.1.4 2.3.6 3.6.6.6 0 1 .4 1 1V20c0 .6-.4 1-1 1C10.6 21 3 13.4 3 4c0-.6.4-1 1-1h3.5c.6 0 1 .4 1 1 0 1.3.2 2.5.6 3.6.1.3 0 .7-.2 1z"/></svg>Contact</div>
</nav>

<!-- Hero -->
<section class="section hero">
  <div class="photo" role="img" aria-label="Plated appetisers served on white spoons against a dark table" style="inset:0;background:linear-gradient(100deg,#050505 0%,#0d0d0d 40%,#2a2724 62%,#4a3a30 78%,#1a1715 100%)"></div>
  <svg class="abs" style="left:22px;top:235px" width="20" height="50" viewBox="0 0 20 50" aria-hidden="true"><path d="M16 4L4 25l12 21" fill="none" stroke="#ffffff" stroke-opacity=".6" stroke-width="2"/></svg>
  <svg class="abs" style="left:1158px;top:235px" width="20" height="50" viewBox="0 0 20 50" aria-hidden="true"><path d="M4 4l12 21L4 46" fill="none" stroke="#ffffff" stroke-opacity=".6" stroke-width="2"/></svg>
  <h1 class="abs hero-title">Good Wholesome Food<br>For the Mind &amp; Body in<br>Millbrook Cafe</h1>
  <div class="search">
    <div class="search-field">Search....</div>
    <div class="search-btn"><svg width="24" height="24" viewBox="0 0 24 24" aria-hidden="true"><circle cx="10" cy="10" r="6.5" fill="none" stroke="#fff" stroke-width="2.5"/><path d="M15 15l6 6" stroke="#fff" stroke-width="2.5"/></svg></div>
  </div>
</section>

<!-- Offers strip -->
<section class="section offers">
  <div class="abs offer-kicker" style="left:148px">Special offers and discount</div>
  <div class="abs offer-title" style="left:268px">Order Online</div>
  <div class="abs offer-line" style="left:175px">www.MillbrookCafe.com</div>
  <svg class="abs" style="left:390px;top:78px" width="42" height="42" viewBox="0 0 24 24" aria-hidden="true"><path fill="none" stroke="#f7b916" stroke-width="1.6" d="M2 4h3l3 11h11l2-8H6"/><circle cx="9" cy="19" r="1.6" fill="#f7b916"/><circle cx="17" cy="19" r="1.6" fill="#f7b916"/></svg>
  <div class="photo" role="img" aria-label="Plated dish on a golden footed serving stand" style="left:478px;top:10px;width:242px;height:143px;border-radius:50% 50% 40% 40%;background:radial-gradient(ellipse at 50% 40%,#b8492a 0%,#8c3a22 45%,#d9a133 70%,rgba(217,161,51,0) 72%)"></div>
  <svg class="abs" style="left:730px;top:78px" width="42" height="42" viewBox="0 0 24 24" aria-hidden="true"><path fill="none" stroke="#f7b916" stroke-width="1.6" d="M6.6 10.8c1.4 2.8 3.8 5.1 6.6 6.6l2.2-2.2c.3-.3.7-.4 1-.2 1.1.4 2.3.6 3.6.6.6 0 1 .4 1 1V20c0 .6-.4 1-1 1C10.6 21 3 13.4 3 4c0-.6.4-1 1-1h3.5c.6 0 1 .4 1 1 0 1.3.2 2.5.6 3.6.1.3 0 .7-.2 1z"/></svg>
  <div class="abs offer-kicker" style="left:800px">Stay up to date with current events</div>
  <div class="abs offer-title" style="left:800px">Order by Phone</div>
  <div class="abs offer-line" style="left:800px">555 014 7890</div>
</section>

<!-- Welcome -->
<section class="section welcome">
  <h2 class="section-title" style="top:50px"><span class="lead">Welcome To</span> <span class="tail">Millbrook Cafe</span></h2>
  <div class="photo" role="img" aria-label="Stir-fried dish with fresh herbs on a black plate" style="left:397px;top:128px;width:403px;height:207px;background:radial-gradient(ellipse at 50% 45%,#8a3b20 0%,#5c2a16 40%,#1c1c1c 62%,rgba(28,28,28,0) 64%)"></div>
  <p class="intro-col" style="left:153px">Lorem Ipsum is simply dummy text of the printing and typesetting industry. Lorem Ipsum has been the industry's standard dummy text ever since the 1500s, when an unknown printer took a galley of type and scrambled it to make a type specimen book. It has survived not only five centuries, but also the leap into electronic typesetting.</p>
  <p class="intro-col" style="left:612px">Lorem Ipsum is simply dummy text of the printing and typesetting industry. Lorem Ipsum has been the industry's standard dummy text ever since the 1500s, when an unknown printer took a galley of type and scrambled it to make a type specimen book. It has survived not only five centuries, but also the leap into electronic typesetting.</p>
  <div class="btn" style="left:515px;top:509px;width:172px;height:59px">Know More</div>
</section>

<!-- Menu -->
<section class="section menu on-dark">
  <div class="photo" role="img" aria-label="Dim restaurant dining room with hanging lamps" style="inset:0;background:linear-gradient(180deg,#2a1f17 0%,#1a130e 50%,#241a12 100%)"></div>
  <h2 class="section-title" style="top:55px"><span class="lead">Our</span> <span class="tail">Menu</span></h2>
  <div class="menu-grid">
    <div class="menu-tile yellow"><h3>Breakfast</h3><p>View All Breakfast Menu</p></div>
    <div class="photo" role="img" aria-label="Table set with wine glasses and a salad plate" style="position:relative;background:linear-gradient(135deg,#d8d4cc,#8f8a80 55%,#4f5a33)"></div>
    <div class="menu-tile yellow"><h3>Dinner</h3><p>View All Breakfast Menu</p></div>
    <div class="photo" role="img" aria-label="Pasta dish with glasses of beer" style="position:relative;background:linear-gradient(135deg,#3b2a1e,#a4522c 50%,#d08a3a)"></div>
    <div class="menu-tile red"><h3>Lunch</h3><p>View All Breakfast Menu</p></div>
    <div class="photo" role="img" aria-label="Roasted main course topped with greens" style="position:relative;background:linear-gradient(135deg,#2d3322,#5e3a22 50%,#7a8a4a)"></div>
  </div>
</section>

<!-- Opening hours -->
<section class="section hours">
  <h2 class="abs script hours-title"><span class="lead">Opening</span> <span class="tail">Hours</span></h2>
  <p class="abs hours-text">Lorem Ipsum is simply dummy text of the printing and typesetting industry. Lorem Ipsum has been the industry.</p>
  <svg class="abs" style="left:546px;top:51px" width="108" height="108" viewBox="0 0 108 108" aria-hidden="true"><circle cx="54" cy="54" r="50" fill="none" stroke="#f7b916" stroke-width="2.5"/><path d="M54 20v34l22 14" fill="none" stroke="#f7b916" stroke-width="2.5"/></svg>
  <div class="hours-row" style="top:62px">Monday to Friday<span>:&nbsp; 08am - 11pm</span></div>
  <div class="hours-row" style="top:96px">Saturday<span>:&nbsp; 10am - 10pm</span></div>
  <div class="hours-row" style="top:132px">Sunday<span>:&nbsp; 11am - 10pm</span></div>
</section>

<!-- Events -->
<section class="section events">
  <h2 class="section-title" style="top:48px"><span class="lead">Latest</span> <span class="tail">Events</span></h2>
  <article class="event" style="left:80px">
    <div class="photo event-photo" role="img" aria-label="Crowd holding signs at an evening rally" style="background:linear-gradient(135deg,#1b2a8a,#3a52c8 50%,#111a55)"></div>
    <div class="event-date"><b>17</b><small>June</small></div>
    <h3 class="event-title">Lorem Ipsum is simply dummy text of the printing and.</h3>
    <p class="event-body">Lorem Ipsum is simply dummy text of the printing and typesetting industry. Lorem Ipsum has been the industry's standard dummy text ever</p>
    <div class="event-more">Readmore.. &#187;</div>
  </article>
  <article class="event" style="left:435px">
    <div class="photo event-photo" role="img" aria-label="Busy cafe dining room at night" style="background:linear-gradient(135deg,#2a1d14,#7a5030 50%,#c98e4a)"></div>
    <div class="event-date"><b>21</b><small>March</small></div>
    <h3 class="event-title">Lorem Ipsum is simply dummy text of the printing and.</h3>
    <p class="event-body">Lorem Ipsum is simply dummy text of the printing and typesetting industry. Lorem Ipsum has been the industry's standard dummy text ever</p>
    <div class="event-more">Readmore.. &#187;</div>
  </article>
  <article class="event" style="left:792px">
    <div class="photo event-photo" role="img" aria-label="Black and white photo of a group of guests" style="background:linear-gradient(135deg,#3a3a3a,#9a9a9a 50%,#1e1e1e)"></div>
    <div class="event-date"><b>23</b><small>March</small></div>
    <h3 class="event-title">Lorem Ipsum is simply dummy text of the printing and.</h3>
    <p class="event-body">Lorem Ipsum is simply dummy text of the printing and typesetting industry. Lorem Ipsum has been the industry's standard dummy text ever</p>
    <div class="event-more">Readmore.. &#187;</div>
  </article>
</section>

<!-- Gallery -->
<section class="section gallery on-dark">
  <div class="photo" role="img" aria-label="Dark blurred dining table with plates" style="inset:0;background:linear-gradient(180deg,#151210 0%,#2b2420 60%,#3b322c 100%)"></div>
  <h2 class="section-title" style="top:65px"><span class="lead">Our</span> <span class="tail">Gallery</span></h2>
  <div class="gallery-row">
    <div class="photo" role="img" aria-label="Historic black and white photo of cafe regulars" style="background:linear-gradient(135deg,#cfcfcf,#6e6e6e 55%,#2d2d2d)"></div>
    <div class="photo" role="img" aria-label="Historic photo of the cafe with a flag, highlighted" style="background:linear-gradient(135deg,#c23a32,#e8403a 55%,#a82c26);display:flex;align-items:center;justify-content:center"><svg width="46" height="46" viewBox="0 0 24 24" aria-hidden="true"><circle cx="10" cy="10" r="7" fill="none" stroke="#fff" stroke-width="2"/><path d="M15 15l6 6M10 6.5v7M6.5 10h7" stroke="#fff" stroke-width="2"/></svg></div>
    <div class="photo" role="img" aria-label="Fresh salad with dressing on a white plate" style="background:linear-gradient(135deg,#d9d2c4,#6f8a3c 50%,#3e2a1e)"></div>
    <div class="photo" role="img" aria-label="Vintage black and white photo of a voting campaign" style="background:linear-gradient(135deg,#e6e2da,#8c8c8c 55%,#3a3a3a)"></div>
  </div>
  <div class="btn" style="left:515px;top:416px;width:170px;height:54px">View All</div>
</section>

<!-- Newsletter -->
<section class="section newsletter">
  <h2 class="abs script news-title"><span class="lead">Our</span> Newsletter</h2>
  <div class="news-field">Enter Email*<svg width="20" height="16" viewBox="0 0 20 16" aria-hidden="true"><rect x="1" y="1" width="18" height="14" fill="none" stroke="#e8403a" stroke-width="1.6"/><path d="M1 1l9 7 9-7" fill="none" stroke="#e8403a" stroke-width="1.6"/></svg></div>
  <div class="btn" style="left:902px;top:61px;width:167px;height:57px">Subscribe</div>
</section>

<!-- Footer -->
<footer class="section footer">
  <div class="photo" role="img" aria-label="Cafe interior in warm yellow tones" style="inset:0;background:linear-gradient(180deg,#f2b416 0%,#f6c33a 50%,#eaa80e 100%)"></div>
  <div class="footer-brand"><span class="brand-name">Millbrook Cafe</span></div>
  <div class="social" style="left:540px"></div>
  <div class="social" style="left:604px"></div>
  <div class="footer-links"><span>Home</span><span>About</span><span>Menu</span><span>Events</span><span>Gallery</span><span>Online Order</span><span>Contact</span></div>
  <div class="copyright">@Millbrook Cafe - 2017 All Rights Reserved</div>
</footer>

</body>
</html>
```